Business card design needed

I am branching out into the world of private practice in Speech Pathology. My clients will be aged 0-17; the business card will be distributed within my existing teacher and parent networks in schools.

I work with clients to develop their speech, language, literacy, fluency, swallowing and voice. I like to think that parents hand over their money to me because I've offered a fun session with positive outcomes/growth and for an affordable price.

I'm flexible with colours; though think something bright would be ideal. I'm not wanting anything too cutesy or 'little kid'. I'd like for it to stand out in a bulging purse or on a fridge crammed with papers.

Industry/Entity Type

Teacher

Contact Information for Business Card

Wren Hollow Speech Pathology Pty Ltd
Molly Fenwick
Speech Pathologist
Ph: 0419 826 307
Email: mollyfenwick@quillpost.com

Logo Text

Logo styles of interest
Character Logo
Wordmark Logo
Lettermark Logo
Requirements
Must have
• A kind of graphic to represent the core business - that is, providing intervention to children 0-17 with communication needs (e.g., speech, language, literacy, swallowing, voice, fluency)

Should not have
• Pictures of babies or children.
Love hearts.

```html
<!DOCTYPE html>
<html lang="en">
<head>
<meta charset="utf-8">
<title>Wren Hollow Speech Pathology – Business Cards</title>
<link rel="stylesheet" href="https://fonts.googleapis.com/css2?family=Jost:wght@300;400;500&display=swap">
<style>
  :root {
    --page: #ffffff;
    --card-edge: #2a2a2a;
    --navy: #263f99;
    --sky: #00adef;
    --accent: #f7941d;
    --white: #ffffff;
  }
  * { margin: 0; padding: 0; box-sizing: border-box; }
  html, body {
    width: 1200px; height: 1000px; overflow: hidden;
    background: var(--page);
    font-family: "Jost", "Futura", sans-serif;
  }
  .canvas { position: relative; width: 1200px; height: 1000px; }
  .card {
    position: absolute;
    width: 682px; height: 390px;
    border: 2px solid var(--card-edge);
    background: var(--white);
    overflow: hidden;
  }
  .card--classic { left: 259px; top: 59px; }
  .card--accent { left: 261px; top: 549px; }
  .brand {
    position: absolute; left: 27px; top: 34px;
    color: var(--navy);
    font-weight: 500;
    font-size: 44px;
    line-height: 58px;
    letter-spacing: 2px;
    text-transform: uppercase;
  }
  .brand-mark {
    position: absolute; left: 410px; top: 40px;
    width: 44px; height: 44px;
    border-radius: 4px;
    background: var(--sky);
  }
  .card--accent .brand-mark { background: var(--accent); }
  .brand-suffix {
    position: absolute; left: 578px; top: 176px;
    color: var(--navy);
    font-weight: 300;
    font-size: 23px;
    letter-spacing: 0.5px;
  }
  .contact-band {
    position: absolute; left: 0; right: 0; bottom: 0;
    height: 154px;
    background: var(--sky);
    border-top: 2px solid var(--navy);
    color: var(--white);
  }
  .holder { position: absolute; left: 0; right: 0; top: 18px; text-align: center; }
  .holder-name { font-size: 27px; font-weight: 500; line-height: 34px; letter-spacing: 0.3px; }
  .holder-role { font-size: 22px; font-weight: 500; line-height: 28px; }
  .detail {
    position: absolute; top: 98px;
    font-size: 22px; font-weight: 500; letter-spacing: 0.2px;
  }
  .detail--phone { left: 25px; }
  .detail--email { right: 22px; }
  .card--accent .detail--email { right: auto; left: 285px; }
  .detail-label { color: var(--accent); }
</style>
</head>
<body>
<main class="canvas">

  <section class="card card--classic">
    <div class="brand">Wren Hollow<br>Speech<br>Pathology</div>
    <div class="brand-mark" role="img" aria-label="Practice mark"></div>
    <div class="brand-suffix">Pty Ltd</div>
    <div class="contact-band">
      <div class="holder">
        <div class="holder-name">Molly Fenwick,</div>
        <div class="holder-role">Speech Pathologist</div>
      </div>
      <div class="detail detail--phone">Ph: 0419.826.307</div>
      <div class="detail detail--email">Email: mollyfenwick@quillpost.com</div>
    </div>
  </section>

  <section class="card card--accent">
    <div class="brand">Wren Hollow<br>Speech<br>Pathology</div>
    <div class="brand-mark" role="img" aria-label="Practice mark"></div>
    <div class="brand-suffix">Pty Ltd</div>
    <div class="contact-band">
      <div class="holder">
        <div class="holder-name">Molly Fenwick,</div>
        <div class="holder-role">Speech Pathologist</div>
      </div>
      <div class="detail detail--phone"><span class="detail-label">p.</span> 0419.826.307</div>
      <div class="detail detail--email"><span class="detail-label">e.</span> mollyfenwick@quillpost.com</div>
    </div>
  </section>

</main>
</body>
</html>
```